Hadley & Partners, LLC Business Card 2016

We need a new business card design for a very important trade show coming up.

We are a compliance Consulting Firm. Our clients are stock brokerage firms and investment advisers.

I would like our logo on both sides of the card.

Info in the front of the card shold include:

Logo
First & Last Name
Title
Office #
Cell #
Email
Company Address (42 W. Calloway St., Suite 300 Pasadena, CA 91417

Back of the card should include the logo and url: www.hadleypartnersgroup.com

Target Market(s)

Stock Brokerage Firms and Investment Advisers

Industry/Entity Type

Financial Service

Contact Information for Business Card

Marcus J. Pellew
President
42 W. Calloway St., Suite 300
Pasadena, CA 91417
O 626.555.0147 ext. 204
C 818.555.0193
Email: marcus@hadleypartnersgroup.com
www.hadleypartnersgroup.com

Requirements
Nice to have
• The back of the card could be black with the logo with the white letters.
• I do want the front of the card to at least have the color logo with the black "Hadley & Partners Lettering.

```html
<!DOCTYPE html>
<html lang="en">
<head>
<meta charset="utf-8">
<title>Hadley &amp; Partners — Business Card</title>
<link rel="stylesheet" href="https://fonts.googleapis.com/css2?family=Cinzel:wght@400;600&family=Questrial&display=swap">
<style>
  :root {
    --bg: #e6e6e6;
    --ink: #111111;
    --paper: #ffffff;
    --red: #d2302a;
    --grey-text: #222222;
  }
  * { margin: 0; padding: 0; box-sizing: border-box; }
  html, body { width: 1200px; height: 900px; overflow: hidden; }
  body {
    background: var(--bg);
    position: relative;
    font-family: "Questrial", "Century Gothic", sans-serif;
  }
  .card {
    position: absolute;
    left: 290px;
    width: 620px;
    height: 354px;
    box-shadow: 0 6px 18px rgba(0,0,0,0.22);
    overflow: hidden;
  }
  .card--back { top: 64px; background: var(--ink); color: var(--paper); }
  .card--front { top: 482px; background: var(--paper); color: var(--grey-text); }

  .brand {
    display: flex;
    align-items: center;
    gap: 16px;
  }
  .brand__mark { width: 34px; height: 34px; background: var(--red); flex: none; }
  .brand__name {
    font-family: "Cinzel", serif;
    font-weight: 600;
    letter-spacing: 0.04em;
    white-space: nowrap;
  }

  .card--back .brand { position: absolute; left: 0; right: 0; top: 130px; justify-content: center; }
  .card--back .brand__mark { width: 46px; height: 46px; }
  .card--back .brand__name { font-size: 40px; color: var(--paper); }
  .back__url {
    position: absolute; left: 0; right: 0; top: 268px;
    text-align: center; font-size: 15px; letter-spacing: 0.12em;
  }

  .card--front .brand { position: absolute; left: 36px; top: 34px; gap: 12px; }
  .card--front .brand__mark { width: 26px; height: 26px; }
  .card--front .brand__name { font-size: 24px; color: var(--ink); }

  .swoosh { position: absolute; inset: 0; width: 620px; height: 354px; }

  .person { position: absolute; left: 36px; top: 118px; }
  .person__name {
    font-family: "Cinzel", serif;
    font-weight: 600;
    font-size: 28px;
    color: var(--red);
    letter-spacing: 0.03em;
  }
  .person__title { font-size: 14px; font-weight: 700; letter-spacing: 0.05em; margin-top: 2px; }

  .contact { position: absolute; left: 36px; top: 196px; list-style: none; font-size: 13.5px; letter-spacing: 0.06em; }
  .contact li { display: flex; align-items: center; gap: 12px; height: 22px; }
  .contact svg { width: 14px; height: 14px; flex: none; }
  .contact .address { padding-left: 26px; height: 18px; }
  .contact .address:first-of-type { margin-top: 6px; }
</style>
</head>
<body>

<section class="card card--back" aria-label="Card back">
  <div class="brand">
    <span class="brand__mark"></span>
    <span class="brand__name">Hadley &amp; Partners</span>
  </div>
  <p class="back__url">www.hadleypartnersgroup.com</p>
</section>

<section class="card card--front" aria-label="Card front">
  <svg class="swoosh" viewBox="0 0 620 354" aria-hidden="true">
    <path d="M520,0 Q560,210 400,354 L620,354 L620,0 Z" fill="var(--red)"/>
    <path d="M575,0 Q585,220 440,354 L620,354 L620,0 Z" fill="var(--ink)"/>
  </svg>

  <div class="brand">
    <span class="brand__mark"></span>
    <span class="brand__name">Hadley &amp; Partners</span>
  </div>

  <div class="person">
    <p class="person__name">Marcus J. Pellew</p>
    <p class="person__title">President</p>
  </div>

  <ul class="contact">
    <li>
      <svg viewBox="0 0 14 14" aria-hidden="true"><path d="M3 1 L5.5 1 L6.5 4 L5 5.2 Q6.5 8.2 8.8 9 L10 7.5 L13 8.5 L13 11 Q12.5 13 10.5 13 Q2 11.5 1 3.5 Q1 1 3 1 Z" fill="var(--red)"/></svg>
      <span>626.555.0147 ext. 204</span>
    </li>
    <li>
      <svg viewBox="0 0 14 14" aria-hidden="true"><rect x="3.5" y="1" width="7" height="12" rx="1" fill="none" stroke="var(--red)" stroke-width="1.6"/></svg>
      <span>818.555.0193</span>
    </li>
    <li>
      <svg viewBox="0 0 14 14" aria-hidden="true"><rect x="1" y="3" width="12" height="8.5" fill="none" stroke="var(--red)" stroke-width="1.5"/><path d="M1 3 L7 8 L13 3" fill="none" stroke="var(--red)" stroke-width="1.5"/></svg>
      <span>marcus@hadleypartnersgroup.com</span>
    </li>
    <li>
      <svg viewBox="0 0 14 14" aria-hidden="true"><circle cx="7" cy="7" r="5.8" fill="var(--red)"/><path d="M1.5 7 H12.5 M7 1.2 Q3.5 7 7 12.8 M7 1.2 Q10.5 7 7 12.8" fill="none" stroke="var(--paper)" stroke-width="0.9"/></svg>
      <span>www.hadleypartnersgroup.com</span>
    </li>
    <li class="address">42 W. Calloway St., Suite 300</li>
    <li class="address">Pasadena, CA 91417</li>
  </ul>
</section>

</body>
</html>
```